Dune Loop needs some awesome stationary

Do you have what it takes to get my brand? You either do or you don't, have a crack at a design and you my just win my business.

I don't want to waste your or my time, so put your creative genius on either a business card or envelope.

I however need a package of stationary that follows the same brand. I will message you to complete the remaining should I like your first submission.

Here is what I need, have a go!

Basically I need the following for my small business based in melbourne.
- Letterhead (printer ready and MS Word)
- Business Card
- Compliments Slip
- Envelope
- Proposal Cover Page (MS Word only)
- Presentation Folder
- Harbor Tally Cards
- Student Name Tent
- Index Cards
- Tack-Pad

I am establishing the brand and it must be modern, professional but also relaxed; that is not formal and not corporate. It represents a company are leaders, but small enough to care and operate like a bunch of friends. We are bringing people and conversations back to business, and turfing out all the bureaucracy and crazy and wasteful procedures. Its about "lets talk and figure it out together and find even better ways".

Target Market(s)

Mainly companies that build software products, but Agile practices are used in many other industries (even graphic design projects)

Industry/Entity Type

Information Technology

Font styles to use
Sans Serif

Colors
3176b5
aaaaaa

Requirements
Must have
• I like curves and circles and not boxes or rectangles.
• I want a colour rich design with my brand colours, but it must be balanced.
• I want more modern than traditional, but simple modern
Should not have
• Not corporate
• Please don't waste my time if your not going to think about it.
• Don't mess with my primary logo
• Don't change my colours
• Don't overlay logo on image

```html
<!DOCTYPE html>
<html lang="en">
<head>
<meta charset="utf-8">
<title>Dune Loop – Business Card</title>
<link rel="stylesheet" href="https://fonts.googleapis.com/css2?family=Source+Sans+3:wght@400;600;700&display=swap">
<style>
  :root {
    --brand-blue: #2c5aa0;
    --brand-grey: #97a0ae;
    --paper: #ffffff;
    --backdrop: #939393;
    --card-shadow: rgba(0, 0, 0, 0.35);
  }
  * { margin: 0; padding: 0; box-sizing: border-box; }
  html, body {
    width: 1200px;
    height: 987px;
    overflow: hidden;
    background: var(--backdrop);
    font-family: "Source Sans 3", sans-serif;
  }
  .stage { position: relative; width: 1200px; height: 987px; }

  .card {
    position: absolute;
    width: 616px;
    height: 352px;
    background: var(--brand-blue);
    box-shadow: 2px 3px 5px var(--card-shadow);
    overflow: hidden;
    color: var(--paper);
  }
  .card--front { left: 293px; top: 130px; }
  .card--back  { left: 292px; top: 505px; height: 351px; }

  .card__swoosh {
    position: absolute;
    inset: 0;
    width: 100%;
    height: 100%;
  }

  .holder__name {
    position: absolute;
    left: 35px;
    top: 56px;
    font-size: 22px;
    font-weight: 600;
    letter-spacing: 0.3px;
  }
  .holder__role, .holder__address, .holder__contacts {
    position: absolute;
    left: 35px;
    font-size: 16.5px;
    line-height: 22px;
    font-weight: 400;
  }
  .holder__role { top: 83px; }
  .holder__address { top: 141px; }
  .holder__contacts { top: 222px; line-height: 23.5px; list-style: none; }
  .holder__contacts li { display: flex; align-items: center; }
  .contact-icon { width: 14px; height: 14px; margin-right: 11px; flex: none; }

  .brand-name {
    position: absolute;
    font-weight: 700;
    white-space: nowrap;
    transform: translate(-50%, -50%);
  }
  .brand-name--front {
    left: 469px;
    top: 224px;
    font-size: 42px;
    color: var(--brand-blue);
  }
  .brand-name--back {
    left: 50%;
    top: 163px;
    font-size: 56px;
    color: var(--paper);
  }

  .call-to-action {
    position: absolute;
    left: 0;
    right: 0;
    top: 256px;
    text-align: center;
    font-size: 31px;
    font-weight: 600;
    line-height: 37px;
  }
</style>
</head>
<body>
<main class="stage">

  <section class="card card--front" aria-label="Business card front">
    <svg class="card__swoosh" viewBox="0 0 526 300" preserveAspectRatio="none" aria-hidden="true">
      <path d="M244,116 C246,210 268,262 302,300 L452,300 C360,278 300,250 270,200 C252,172 244,140 244,116 Z"
            fill="var(--brand-grey)" stroke="var(--paper)" stroke-width="3"/>
      <path d="M305,0 C248,40 232,140 262,198 C292,252 360,282 452,300 L526,300 L526,0 Z"
            fill="var(--paper)"/>
    </svg>

    <h1 class="holder__name">CORIN WALSBY</h1>
    <p class="holder__role">CEO<br>Professional Scrum Trainer</p>
    <p class="holder__address">PO Box 4180<br>Alderbrook North<br>VIC 3990, Australia</p>
    <ul class="holder__contacts">
      <li>
        <svg class="contact-icon" viewBox="0 0 14 14" aria-hidden="true">
          <rect x="3.5" y="0.8" width="7" height="12.4" rx="1.2" fill="none" stroke="var(--paper)" stroke-width="1.4"/>
          <circle cx="7" cy="11" r="0.8" fill="var(--paper)"/>
        </svg>+61 400 123 987
      </li>
      <li>
        <svg class="contact-icon" viewBox="0 0 14 14" aria-hidden="true">
          <rect x="0.5" y="3" width="13" height="8.5" fill="var(--paper)"/>
          <path d="M0.8,3.3 L7,8 L13.2,3.3" fill="none" stroke="var(--brand-blue)" stroke-width="1"/>
        </svg>corin@duneloop.com.au
      </li>
      <li>
        <svg class="contact-icon" viewBox="0 0 14 14" aria-hidden="true">
          <circle cx="7" cy="7" r="6.2" fill="var(--paper)"/>
          <path d="M4,3.5 C5.5,4 6,5.5 5,7 C4.5,8 5.5,9.5 6.5,10 M9,2.5 C8.5,4 9.5,5 10.5,5.5 M8.5,8 C9.5,8.5 10,10 9,11.5"
                fill="none" stroke="var(--brand-blue)" stroke-width="1.1"/>
        </svg>www.duneloop.com.au
      </li>
    </ul>

    <p class="brand-name brand-name--front">Dune Loop</p>
  </section>

  <section class="card card--back" aria-label="Business card back">
    <p class="brand-name brand-name--back">Dune Loop</p>
    <p class="call-to-action">Call Us<br>13 000 DUNES</p>
  </section>

</main>
</body>
</html>
```